Web Design Project - ClipHaven Style Website

Hi there, we want to create a ClipHaven / Falzo style website. We have a logo, and will be using a similar structure to this platform; http://reelpail.example/v2/
Please feel free to be creative as possible, and make the site look however you would like :) keeping in mind the Ad space, and user friendly layout. We would like
1) The main page and
2) the video view page
designed
Logo, and images attached
Updates
Logo and stock image uploaded
Hello; we most likely be basing the site on this reel pail theme, which also works as a mobile version.
Another option that I found for a layout which is different :)
http://www.quarnet-studio.example/demo-theme.cfm?theme=pivota
One last update; really like this one too
I am 100% likely to now use this format;
Target Market(s)
Bars, Cafe's, Restaurants, Attractions, Venues, Pubs, Wine and Dine
Industry/Entity Type
Cliphaven
Requirements
Must have
- Can be similar to ClipHaven, but closer to Falzo's funky fresh look.
Should not have
- Not be too cluttered with too many videos on the home page. Feel free to think outside the box

```html
<!DOCTYPE html>
<html lang="en">
<head>
<meta charset="utf-8">
<title>Harbourline Motion – Video</title>
<link href="https://fonts.googleapis.com/css2?family=Questrial&family=Open+Sans:wght@400;600;700&display=swap" rel="stylesheet">
<style>
:root{
  --cyan:#3ccff2;
  --page:#f7f7f7;
  --band:#e9e9e9;
  --bar:#232323;
  --bar-edge:#1a1a1a;
  --screen:#050001;
  --thumb:#0c0c0c;
  --frame:#000;
  --title:#4f6f93;
  --body:#8a8a8a;
  --dark:#444;
  --ad:#e8e8e8;
  --ad-text:#9d9d9d;
  --photo-a:#2b2e22;
  --photo-b:#cfc9b4;
}
*{box-sizing:border-box;margin:0;padding:0}
html,body{width:1200px;height:1194px;overflow:hidden}
body{position:relative;background:var(--page);font-family:"Open Sans",sans-serif;color:var(--dark)}
.top-rule{position:absolute;left:0;top:0;width:1200px;height:4px;background:var(--cyan)}
.brand{position:absolute;left:218px;top:34px;font-family:"Questrial",sans-serif;font-size:40px;color:var(--cyan);letter-spacing:-0.5px;line-height:1}
.band{position:absolute;left:0;top:112px;width:1200px;height:466px;background:var(--band);border-top:1px solid #e2e2e2}
.nav{position:absolute;left:206px;top:117px;width:765px;height:49px;background:var(--bar);border-top:3px solid var(--bar-edge)}
.nav ul{list-style:none;display:flex;position:absolute;left:23px;top:13px;font-family:"Questrial",sans-serif;font-size:13px;color:#d6d6d6}
.nav li{margin-right:19px}
.nav li.active{color:var(--cyan);font-weight:700;margin-right:23px}
.search{position:absolute;left:595px;top:13px;width:154px;height:17px;background:linear-gradient(#fff,#ddd);font-size:9px;color:#999;padding:2px 4px}
.search-go{position:absolute;right:0;top:0;width:19px;height:17px;background:var(--cyan)}
.screen{position:absolute;left:219px;top:166px;width:739px;height:346px;background:var(--screen)}
.play{position:absolute;left:349px;top:142px}
.strip{position:absolute;left:206px;top:512px;width:765px;height:72px;background:var(--bar)}
.strip .thumb{position:absolute;top:13px;width:74px;height:50px;background:var(--thumb)}
.strip svg.arrow{position:absolute;top:26px}
.content{position:absolute;left:219px;top:584px;width:739px;height:597px;background:#fafafa;border:3px solid var(--frame);border-top:none}
.video-title{position:absolute;left:31px;top:21px;font-size:15px;font-weight:700;color:var(--title)}
.meta{position:absolute;left:31px;top:40px;font-size:7.5px;color:#555}
.desc{position:absolute;left:31px;top:53px;width:400px;font-size:9.5px;line-height:12.5px;color:var(--body)}
.comments-head{position:absolute;left:31px;top:133px;font-size:11px;color:var(--title)}
.avatar{position:absolute;left:31px;top:151px;width:42px;height:42px;background:linear-gradient(135deg,#8b6b58,#e3c3ad)}
.comment-box{position:absolute;left:85px;top:151px;width:317px;height:42px;border:1px solid #ddd;background:#fff;font-size:8px;color:#aaa;padding:3px 10px}
.comment{position:absolute;left:31px;width:376px;font-size:8px;line-height:10.7px;color:#555}
.comment .by{display:block;margin-top:5px;color:#666}
.comment .by span{margin-left:12px}
.ad{position:absolute;left:499px;top:21px;width:218px;height:134px;background:var(--ad);display:flex;align-items:center;justify-content:center;font-size:14px;color:var(--ad-text)}
.side-item{position:absolute;left:499px;width:230px;height:51px}
.side-item .pic{position:absolute;left:0;top:0;width:75px;height:51px;background:linear-gradient(120deg,var(--photo-a) 10%,var(--photo-b) 50%,var(--photo-a) 90%)}
.side-item p{position:absolute;left:80px;top:2px;font-size:8px;line-height:10.5px;color:#555;width:150px}
.side-item small{position:absolute;left:80px;top:31px;font-size:7px;line-height:9.5px;color:#666}
</style>
</head>
<body>
<div class="top-rule"></div>
<div class="brand">Harbourline Motion</div>
<div class="band"></div>

<nav class="nav">
  <ul>
    <li class="active">Home</li><li>My Channel</li><li>Likes</li><li>Videos</li><li>Watch Later</li><li>TV Shows</li><li>Movies</li><li>Upload</li>
  </ul>
  <div class="search">search
    <div class="search-go"><svg width="19" height="17"><circle cx="9.5" cy="8.5" r="5" fill="#fff"/><path d="M8 6l3.5 2.5L8 11z" fill="#3ccff2"/></svg></div>
  </div>
</nav>

<div class="screen">
  <svg class="play" width="52" height="52"><circle cx="26" cy="26" r="26" fill="#eee"/><path d="M21 15l14 11-14 11z" fill="#111"/></svg>
</div>

<div class="strip">
  <svg class="arrow" style="left:8px" width="10" height="20"><path d="M8 1L2 10l6 9" stroke="#444" stroke-width="2.5" fill="none"/></svg>
  <div class="thumb" style="left:26px"></div>
  <div class="thumb" style="left:117px"></div>
  <div class="thumb" style="left:208px"></div>
  <div class="thumb" style="left:299px"></div>
  <div class="thumb" style="left:390px"></div>
  <div class="thumb" style="left:481px"></div>
  <div class="thumb" style="left:571px"></div>
  <div class="thumb" style="left:662px"></div>
  <svg class="arrow" style="left:747px" width="10" height="20"><path d="M2 1l6 9-6 9" stroke="#444" stroke-width="2.5" fill="none"/></svg>
</div>

<main class="content">
  <h1 class="video-title">Video Title</h1>
  <div class="meta">Published on May 23, 2012 by brightreelco</div>
  <p class="desc">This is Lumenbox's version of Lorem Ipsum. Proin gravida nibh vel velit auctor aliquet. Aenean sollicitudin, lorem quis bibendum auctor, nisi elit consequat ipsum, nec sagittis sem nibh id elit. Duis sed odio sit amet nibh vulputate cursus a sit amet mauris. Morbi accumsan ipsum velit. Nam nec tellus a odio tincidunt que.</p>

  <h2 class="comments-head">All Comments (37)</h2>
  <div class="avatar" role="img" aria-label="Commenter profile photo"></div>
  <div class="comment-box">Add a Comment</div>

  <div class="comment" style="top:211px">This is Lumenbox's version of Lorem Ipsum. Proin gravida nibh vel velit auctor aliquet. Aenean sollicitudin, lorem quis bibendum auctor, nisi elit consequat ipsum, nec sagittis sem nibh id elit. Duis sed odio sit amet nibh vulputate cursus a sit amet mauris. Morbi accumsan ipsum velit.<span class="by">user124asdf<span>1 hour ago</span></span></div>
  <div class="comment" style="top:264px">Sed non mauris vitae erat consequat auctor eu in elit. Class aptent taciti sociosqu ad litora torquent per conubia nostra, per inceptos himenaeos. Mauris in erat justo. Nullam ac urna eu felis dapibus condimentum sit amet a augue. Sed non neque elit. Sed ut imperdiet nisi. Proin condimentum fermentum nunc. Etiam pharetra, erat sed fermentum feugiat, velit mauris egestas quam, ut aliquam massa nisl quis neque. Suspendisse in orci enim.<span class="by">user124asdf<span>1 hour ago</span></span></div>
  <div class="comment" style="top:350px">This is Lumenbox's version of Lorem Ipsum. Proin gravida nibh vel velit auctor aliquet. Aenean sollicitudin, lorem quis bibendum auctor, nisi elit consequat ipsum, nec sagittis sem nibh id elit. Duis sed odio sit amet nibh vulputate cursus a sit amet mauris. Morbi accumsan ipsum velit. auctor eu in elit.<span class="by">user124asdf<span>1 hour ago</span></span></div>

  <div class="ad">space for ads</div>

  <div class="side-item" style="top:164px"><div class="pic" role="img" aria-label="Video thumbnail of white tulips"></div><p>This is Lumenbox's version of Lorem Ipsum.</p><small>uploaded by user2345<br>34,342 views</small></div>
  <div class="side-item" style="top:224px"><div class="pic" role="img" aria-label="Video thumbnail of white tulips"></div><p>This is Lumenbox's version of Lorem Ipsum.</p><small>uploaded by user2345<br>34,342 views</small></div>
  <div class="side-item" style="top:284px"><div class="pic" role="img" aria-label="Video thumbnail of white tulips"></div><p>This is Lumenbox's version of Lorem Ipsum.</p><small>uploaded by user2345<br>34,342 views</small></div>
  <div class="side-item" style="top:344px"><div class="pic" role="img" aria-label="Video thumbnail of white tulips"></div><p>This is Lumenbox's version of Lorem Ipsum.</p><small>uploaded by user2345<br>34,342 views</small></div>
  <div class="side-item" style="top:404px"><div class="pic" role="img" aria-label="Video thumbnail of white tulips"></div><p>This is Lumenbox's version of Lorem Ipsum.</p><small>uploaded by user2345<br>34,342 views</small></div>
  <div class="side-item" style="top:464px"><div class="pic" role="img" aria-label="Video thumbnail of white tulips"></div><p>This is Lumenbox's version of Lorem Ipsum.</p><small>uploaded by user2345<br>34,342 views</small></div>
  <div class="side-item" style="top:524px"><div class="pic" role="img" aria-label="Video thumbnail of white tulips"></div><p>This is Lumenbox's version of Lorem Ipsum.</p><small>uploaded by user2345<br>34,342 views</small></div>
</main>
</body>
</html>
```